Mira Tails

im a dog walker, pet sitter and dog groomer. I can look after all pets from once a day pop in feeds of cats to small holdings and exotics. have 10 years experience in the industry. I can look after peoples dogs for the day while they are out or for longer if on holiday. I walk dogs when people are at work so the dogs get to have fun too. I do house sitting so all your animals are looked after together. you have designed my business cards and I wanted the 'mira tails' with the paw to be the same on the leaflets. I have spoken to printolane and they have sent a pdf file of business card and said it can be cropped. please let me know if this cant be done
im also a qualified canine hydrotherapist

Target Market(s)

pet owners

Industry/Entity Type

Pet

Requirements
Must have
• my phone number 07834562719
• email miratails@mailbox-example.co.uk
• area; Tunbridge wells, Sevenoaks and surrounding areas
• I want it almost done as bullet points with the main things being the dog walking and the pet sitting.
Nice to have
• cartoon animals like business card not the cartoons with big eyes

```html
<!DOCTYPE html>
<html lang="en">
<head>
<meta charset="utf-8">
<title>Mira Tails – Pet Care Leaflet</title>
<link href="https://fonts.googleapis.com/css2?family=Lobster+Two:wght@400;700&family=Source+Sans+3:wght@600;700&display=swap" rel="stylesheet">
<style>
  :root {
    --paper: #f4f4f2;
    --grass-light: #b7d97a;
    --grass-mid: #7fb93f;
    --grass-dark: #4f8f22;
    --purple: #7a4fa0;
    --purple-deep: #653c8c;
    --sun: #f4c531;
    --badge-red: #e4202e;
    --white: #ffffff;
    --ink: #2b2b2b;
    --logo-ink: #7a4fa0;
    --script: "Lobster Two", cursive;
    --sans: "Source Sans 3", sans-serif;
  }
  * { box-sizing: border-box; margin: 0; padding: 0; }
  html, body { width: 973px; height: 1200px; overflow: hidden; background: #ddd; }
  .leaflet { position: relative; width: 973px; height: 1200px; overflow: hidden; background: var(--paper); }
  .backdrop { position: absolute; inset: 0; }

  .brand { position: absolute; left: 70px; top: 70px; display: flex; align-items: center; gap: 22px; }
  .brand-dot { width: 70px; height: 70px; border-radius: 50%; background: var(--sun); }
  .brand-name { font-family: var(--sans); font-weight: 700; font-size: 72px; line-height: 1; color: var(--logo-ink); }

  .art { position: absolute; }
  .art-animals { left: 560px; top: 20px; width: 390px; height: 400px; border-radius: 40% 40% 20% 30%;
    background: radial-gradient(ellipse at 60% 45%, #8a5a3a 0%, #a9876b 45%, rgba(200,180,150,0) 75%); }
  .art-puppy { left: 30px; top: 330px; width: 390px; height: 390px; border-radius: 45% 45% 20% 20%;
    background: radial-gradient(ellipse at 50% 45%, #2e2e2e 0%, #5b5b5b 40%, rgba(120,120,120,0) 72%); }
  .art-owner { left: 480px; top: 430px; width: 470px; height: 470px; border-radius: 45% 45% 10% 30%;
    background: radial-gradient(ellipse at 55% 50%, #efd9b8 0%, #e08aa0 40%, rgba(200,120,120,0) 72%); }

  .badge { position: absolute; left: 298px; top: 318px; width: 204px; height: 204px; border-radius: 50%;
    background: var(--badge-red); border: 8px solid var(--white); box-shadow: 0 4px 10px rgba(0,0,0,.25);
    display: flex; align-items: center; justify-content: center; text-align: center;
    font-family: var(--script); font-weight: 700; color: var(--white); font-size: 31px; line-height: 1.1; }
  .badge-inner { display: block; }

  .services { position: absolute; left: 52px; top: 752px; list-style: none; }
  .services li { position: relative; padding-left: 48px; font-family: var(--sans); font-weight: 700;
    font-size: 37px; line-height: 51px; color: var(--white); text-shadow: 1px 2px 3px rgba(0,0,0,.45); }
  .services li::before { content: ""; position: absolute; left: 4px; top: 13px; width: 26px; height: 26px;
    border-radius: 50%; background: var(--sun); box-shadow: inset 0 -3px 4px rgba(0,0,0,.2); }

  .area { position: absolute; left: 52px; top: 1020px; font-family: var(--sans); font-weight: 700;
    font-size: 32px; line-height: 46px; color: var(--white); text-shadow: 1px 2px 3px rgba(0,0,0,.45); }

  .qualification { position: absolute; left: 448px; top: 894px; width: 436px; height: 46px;
    background: var(--sun); border-radius: 8px 8px 0 0; font-family: var(--sans); font-weight: 700;
    font-size: 25px; line-height: 46px; text-align: center; color: var(--ink); }

  .contact { position: absolute; left: 410px; top: 936px; width: 522px; height: 244px;
    background: var(--purple); border: 3px solid var(--sun); border-radius: 14px;
    text-align: center; color: var(--white); padding-top: 14px; }
  .contact-name { font-family: var(--script); font-weight: 400; font-size: 74px; line-height: 1.05; }
  .contact-email { font-family: var(--sans); font-weight: 600; font-size: 27px; margin-top: 14px; }
  .contact-phone { font-family: var(--sans); font-weight: 700; font-size: 58px; line-height: 1.1; margin-top: 10px; }
</style>
</head>
<body>
<main class="leaflet">
  <svg class="backdrop" width="973" height="1200" viewBox="0 0 973 1200" aria-hidden="true">
    <defs>
      <linearGradient id="grass" x1="0" y1="0" x2="0" y2="1">
        <stop offset="0" stop-color="var(--grass-light)"/>
        <stop offset="0.5" stop-color="var(--grass-mid)"/>
        <stop offset="1" stop-color="var(--grass-dark)"/>
      </linearGradient>
    </defs>
    <path d="M0,360 C220,280 400,390 600,360 S880,210 973,160 L973,1200 L0,1200 Z" fill="url(#grass)"/>
    <path d="M0,318 C220,238 400,348 600,318 S880,168 973,118" fill="none" stroke="var(--sun)" stroke-width="16"/>
    <path d="M0,342 C220,262 400,372 600,342 S880,192 973,142" fill="none" stroke="var(--purple)" stroke-width="34"/>
  </svg>

  <header class="brand">
    <span class="brand-dot"></span>
    <span class="brand-name">Mira Tails</span>
  </header>

  <div class="art art-animals" role="img" aria-label="Cartoon illustration of a brown dog, cat, chicken, rabbit and frog"></div>
  <div class="art art-puppy" role="img" aria-label="Photo of a black and white puppy standing"></div>
  <div class="art art-owner" role="img" aria-label="Photo of a woman hugging a cream labrador puppy"></div>

  <div class="badge"><span class="badge-inner">10 Years<br>Experience<br>in animal<br>industry</span></div>

  <ul class="services">
    <li>Dog Walking</li>
    <li>Pet/House Sitting</li>
    <li>Dog Grooming</li>
    <li>Small Holder<br>Knowledge</li>
  </ul>

  <p class="area">Tunbridge Wells,<br>Sevenoaks and<br>Surrounding Areas</p>

  <div class="qualification">Qualified Canine Hydrotherapist</div>
  <section class="contact">
    <h2 class="contact-name">Mira Dalton</h2>
    <p class="contact-email">miratails@mailbox-example.co.uk</p>
    <p class="contact-phone">07834.562.719</p>
  </section>
</main>
</body>
</html>
```